A new company focused on starting and investing in transformative businesses.

We need a simple and clean website with a few pages. we like larkmeadow.com as a starting point. we want the landing page to be very simple with an option to click through on the top right into INVESTOR LOGIN. then we want to be able to scroll down to see more about our company.

Target Market(s)

professional

Coding

Coded - Design and coding required

Number of Pages Required

2 page

Font styles to use
Serif
Sans Serif

Requirements
Must have
• HALVERN BUILDERS logo (attached as a file) on the top with INVESTOR LOGIN as a click through on the right. Please model the click through from larkmeadow.com. The description (also written in attached file) should be on the landing page. we do not want to have to scroll to read the description.

Then we can scroll down to read more about Halvern including the mission and the two types of businesses. More is detailed on the attached file called "Halvern Website Syntax"
Should not have
• should not be slow loading with lots of fancy graphics. should not be busy and with too many colors.

```html
<!DOCTYPE html>
<html lang="en">
<head>
<meta charset="utf-8">
<title>Halvern Builders</title>
<link rel="stylesheet" href="https://fonts.googleapis.com/css2?family=Open+Sans:ital,wght@0,400;0,600;0,700;1,400&display=swap">
<style>
:root{
  --blue:#00579b;
  --ink:#231f20;
  --text:#1e1e1e;
  --muted:#555;
  --page:#f4f4f4;
  --white:#ffffff;
  --footer:#231f20;
}
*{margin:0;padding:0;box-sizing:border-box}
html,body{width:960px;height:1200px;overflow:hidden}
body{font-family:"Open Sans",Arial,sans-serif;color:var(--text);background:var(--page);position:relative}
.site-header{position:absolute;left:0;top:0;width:960px;height:84px;background:linear-gradient(#e6e6e6,#f8f8f8)}
.brand{position:absolute;display:flex;align-items:center;gap:7px;font-weight:700;letter-spacing:.5px}
.brand-mark{display:block;background:var(--blue)}
.site-header .brand{left:18px;top:29px;font-size:15px;color:var(--blue)}
.site-header .brand-mark{width:22px;height:22px}
.investor-login{position:absolute;left:792px;top:23px;width:150px;height:39px;border:1px solid var(--blue);display:flex;align-items:center;justify-content:center;gap:7px;font-size:11px;letter-spacing:1.4px;color:#333;text-decoration:none}
.hero{position:absolute;top:84px;left:0;width:960px;height:324px;display:flex}
.hero-panel{position:relative;width:480px;height:324px;overflow:hidden}
.hero-about{background:var(--white)}
.hero-mission{background:var(--blue);color:var(--white)}
.hero-title{position:absolute;top:72px;font-size:30px;font-weight:700;letter-spacing:-1px;line-height:1.2}
.accent-bar{position:absolute;width:36px;height:5px;background:var(--blue)}
.hero-mission .accent-bar{background:var(--white)}
.hero-text{position:absolute;top:158px;width:360px;font-size:15px;line-height:24px;letter-spacing:.2px}
.hero-about .hero-title,.hero-about .accent-bar,.hero-about .hero-text{left:96px}
.hero-mission .hero-title,.hero-mission .accent-bar,.hero-mission .hero-text{left:30px}
.hero .accent-bar{top:112px}
.hero-text{z-index:1}
.ghost-word{position:absolute;left:92px;top:146px;font-size:160px;font-weight:600;color:#f4f4f4;letter-spacing:-4px;line-height:1;white-space:nowrap}
.section-title{position:absolute;top:444px;left:0;width:960px;text-align:center;font-size:20px;font-weight:600;letter-spacing:-.5px;color:var(--ink)}
.business-card{position:absolute;left:96px;width:768px;height:246px;background:var(--white);overflow:hidden}
.ground-up{top:483px}
.special{top:777px}
.card-photo{position:absolute;top:0;width:282px;height:246px}
.ground-up .card-photo{right:0;background:linear-gradient(135deg,#f2d08a 0%,#c98f45 45%,#7a5326 100%)}
.special .card-photo{left:0;background:linear-gradient(135deg,#6f7780 0%,#a3adb8 45%,#7fa3cf 100%)}
.card-body{position:absolute;top:0;width:470px;height:246px}
.ground-up .card-body{left:29px}
.special .card-body{left:312px}
.card-title{position:absolute;left:0;top:22px;font-size:30px;font-weight:600;letter-spacing:-1px;color:var(--ink);white-space:nowrap}
.card-body .accent-bar{left:1px;top:64px}
.card-text{position:absolute;left:1px;top:106px;width:420px;font-size:8.4px;line-height:19.2px;color:var(--muted);z-index:1}
.outline-word{position:absolute;left:-6px;top:92px;font-size:150px;font-weight:400;line-height:1;letter-spacing:6px;color:transparent;-webkit-text-stroke:1px #ececec;white-space:nowrap}
.site-footer{position:absolute;left:0;top:1071px;width:960px;height:129px;background:var(--footer);color:var(--white)}
.site-footer .brand{left:96px;top:20px;font-size:11px;color:var(--white)}
.site-footer .brand-mark{width:16px;height:16px;background:var(--white)}
.footer-note{position:absolute;left:96px;font-size:8.5px;color:#ddd}
.footer-note strong{color:var(--white);font-weight:700}
.footer-contact{top:76px}
.footer-copy{top:93px;color:var(--white)}
</style>
</head>
<body>
<header class="site-header">
  <div class="brand"><span class="brand-mark"></span>HALVERN BUILDERS</div>
  <a class="investor-login" href="#">
    <svg width="10" height="12" viewBox="0 0 10 12" fill="none" stroke="#333" stroke-width="1"><rect x="1" y="5.5" width="8" height="6" rx="1"/><path d="M2.8 5.5V3.6a2.2 2.2 0 0 1 4.4 0v1.9"/></svg>
    INVESTOR LOGIN
  </a>
</header>

<section class="hero">
  <div class="hero-panel hero-about">
    <div class="ghost-word" aria-hidden="true">HALVERN</div>
    <h1 class="hero-title">HALVERN</h1>
    <span class="accent-bar"></span>
    <p class="hero-text">Halvern Builders is an entrepreneurial firm focused on building and growing transformational companies</p>
  </div>
  <div class="hero-panel hero-mission">
    <h2 class="hero-title">MISSION</h2>
    <span class="accent-bar"></span>
    <p class="hero-text" style="width:400px">Our mission is to build meaningful businesses that create enduring value by impacting people in a measurable way.</p>
  </div>
</section>

<h2 class="section-title">Types of Businesses</h2>

<article class="business-card ground-up">
  <div class="card-body">
    <div class="outline-word" aria-hidden="true">GROU</div>
    <h3 class="card-title">Ground Up</h3>
    <span class="accent-bar"></span>
    <p class="card-text">Our ground up business applies a proven analytic process to identify <em>value edge</em>, a form of competitive advantage. We architect transformational companies and are deliberate in creating the foundation necessary to lead an industry.</p>
  </div>
  <div class="card-photo" role="img" aria-label="Runner tying a shoe on a sunlit dirt trail"></div>
</article>

<article class="business-card special">
  <div class="card-photo" role="img" aria-label="Two businessmen shaking hands in an office"></div>
  <div class="card-body">
    <div class="outline-word" aria-hidden="true">SPECIA</div>
    <h3 class="card-title">Special Opportunities</h3>
    <span class="accent-bar"></span>
    <p class="card-text">We partner with exceptional teams that create value by transforming lives. Our investment focus includes large companies and spin-outs.</p>
  </div>
</article>

<footer class="site-footer">
  <div class="brand"><span class="brand-mark"></span>HALVERN BUILDERS</div>
  <p class="footer-note footer-contact">For media inquiries, please contact <strong>press@halvernbuilders.com</strong></p>
  <p class="footer-note footer-copy">© 2020, halvernbuilders, all rights reserved</p>
</footer>
</body>
</html>
```